Tallow Microsystems PowerPoint Master Slide Deck Design

This is a 2-phase project to design a slide deck for a semiconductor company in the Silicon Valley. The design budget will be increased with each phase.
The slide deck will need to have one version with a dark background for presentations and a second version with a white background. Otherwise, the slides will be the same. I anticipate we will need a total of 10 slides, but that number may change.
The first phase will be to design a Title and a Title and Content slide.
- The Title Slide is the first slide of the deck. It should include the presentation title, the presenter's name and date of presentation
- The Title and Content slide should include a title and content with bullet points and up to 2 additional sub-bullets
- The Title and Content slide should have a footer that includes the slide #, Tallow Microsystems Confidential, and the logo. This footer will be on every slide except the Title Slide
The first two slides will serve as the format for the remaining ~8 slides:
-Header and Content Text (1, 2, 4 column)
-Header and Content Image (bar chart, pie chart, tables)
-Break
-Title only
-Closing (Tallow logo only)
Our slides contain a lot of content so a clean and simple design is best.
Both phases will need to include pre-set color options for
-Text and Lines
-Shadows
-Bullets and sub-bullets (including shapes, ex. circle, slash, square, etc.)
-Bar charts, pie charts, tables
Samples of our collateral are attached. Logo files are also attached
Look and feel
Each slider illustrates characteristics of the customer's brand and the style your logo design should communicate.

```html
<!DOCTYPE html>
<html lang="en">
<head>
<meta charset="utf-8">
<title>Tallow Microsystems Slide Deck</title>
<link href="https://fonts.googleapis.com/css2?family=Montserrat:wght@400;500;600;700;800&family=Yellowtail&display=swap" rel="stylesheet">
<style>
:root{
  --ink:#2b2b2b;
  --text:#6a6a6a;
  --blue:#1436e6;
  --blue-deep:#0a1fc4;
  --cyan:#19b6ff;
  --dark-bar:#3a3a3a;
  --stage:#262626;
  --backdrop:#6b6b6b;
  --paper:#fbfbfd;
}
*{margin:0;padding:0;box-sizing:border-box}
html,body{width:1200px;height:4926px;overflow:hidden}
body{background:var(--backdrop);font-family:"Montserrat",sans-serif;position:relative}
.hero{position:absolute;left:0;top:0;width:1200px;height:749px;background:var(--stage);display:flex;align-items:center;justify-content:center}
.hero-name{color:#fff;font-size:44px;font-weight:500;letter-spacing:1px}
.slide{position:absolute;left:241px;width:718px;height:404px;background:var(--paper);overflow:hidden}
.slide::after{content:"";position:absolute;left:0;right:0;bottom:4px;height:6px;background:linear-gradient(90deg,var(--blue-deep),var(--blue) 55%,var(--cyan))}
.slide::before{content:"";position:absolute;left:0;right:0;bottom:0;height:4px;background:#444}
.title{position:absolute;font-weight:800;color:var(--ink);font-size:38px;line-height:1.05;letter-spacing:.3px}
.body{position:absolute;font-size:11px;line-height:1.4;color:var(--text)}
.center{text-align:center;left:0;right:0;margin:auto}
.footer{position:absolute;left:241px;top:362px;display:flex;align-items:center;gap:20px}
.footer-note{font-size:8px;color:#555}
.footer-name{font-size:12px;font-weight:700;color:var(--blue)}
.visual{position:absolute;background:linear-gradient(135deg,var(--blue-deep),var(--blue) 50%,var(--cyan))}
.portrait{position:absolute;left:65px;top:220px;width:88px;height:88px;border-radius:50%;border:3px solid #fff;box-shadow:0 0 0 2px #9aa;background:linear-gradient(160deg,#b68a6c,#4a3a34)}
.presenter{position:absolute;left:170px;top:240px;font-size:19px;color:var(--ink);line-height:1.2}
.date{position:absolute;left:610px;top:366px;font-size:14px;color:#555;letter-spacing:.5px}
.bullets{position:absolute;top:238px;left:52px;display:flex;gap:34px}
.bullet{width:180px;position:relative;padding-left:0}
.bullet-head{display:flex;align-items:center;gap:10px;font-size:17px;font-weight:700;color:var(--ink)}
.sub{margin-left:14px;padding-left:14px;border-left:1px solid #bbb;margin-top:6px}
.sub li{list-style:none;display:flex;align-items:center;gap:6px;font-size:13px;color:#777;line-height:1.55}
.break-mug{position:absolute;left:155px;top:113px;width:160px;height:134px;border-radius:18px 18px 40px 40px;background:linear-gradient(90deg,#222 0%,#eee 45%,#bbb 100%)}
.break-pill{position:absolute;left:266px;top:141px;width:296px;height:80px;border-radius:40px;border:2px solid var(--blue);display:flex;align-items:center;justify-content:center;font-family:"Yellowtail",cursive;font-size:62px;color:var(--ink)}
.closing{position:absolute;left:0;right:0;top:160px;text-align:center;font-size:48px;font-weight:500;color:var(--blue)}
</style>
</head>
<body>

<section class="hero">
  <div class="hero-name">Tallow Microsystems</div>
</section>

<!-- Title slide -->
<section class="slide" style="top:875px">
  <h1 class="title" style="left:65px;top:96px">PRESENTATION<br>TITLE</h1>
  <div class="portrait" role="img" aria-label="Presenter portrait photograph"></div>
  <div class="presenter">Presenter's<br>Name</div>
  <div class="visual" style="left:466px;top:61px;width:252px;height:268px;border-radius:24px 0 0 24px" role="img" aria-label="Blue brand graphic"></div>
  <div class="date">12-12-2023</div>
</section>

<!-- Title and content -->
<section class="slide" style="top:1315px">
  <h2 class="title" style="left:52px;top:60px">SLIDE TITLE</h2>
  <p class="body" style="left:52px;top:108px;width:290px;font-size:10px">Lorem ipsum dolor sit amet, consectetuer adipiscing elit, sed diam nonummy nibh euismod tincidunt ut laoreet dolore magna aliquam erat volutpat. Ut wisi enim ad minim veniam, quis nostrud exerci tation ullamcorper suscipit lobortis nisl ut aliquip ex ea</p>
  <div class="visual" style="left:410px;top:36px;width:256px;height:153px;border-radius:10px" role="img" aria-label="Photograph of two colleagues at a laptop in blue duotone"></div>
  <div class="bullets">
    <div class="bullet">
      <div class="bullet-head"><svg width="22" height="22" viewBox="0 0 22 22"><circle cx="11" cy="11" r="9" fill="none" stroke="#1aa0ff" stroke-width="2"/><circle cx="11" cy="11" r="4" fill="none" stroke="#1436e6" stroke-width="2"/></svg>Bullet Point 1</div>
      <ul class="sub"><li><svg width="12" height="12"><circle cx="6" cy="6" r="5" fill="none" stroke="#777"/><path d="M3.5 6l2 2 3-3.5" fill="none" stroke="#777"/></svg>Sub-bullet point</li><li><svg width="12" height="12"><circle cx="6" cy="6" r="5" fill="none" stroke="#777"/><path d="M3.5 6l2 2 3-3.5" fill="none" stroke="#777"/></svg>Sub-bullet point</li></ul>
    </div>
    <div class="bullet">
      <div class="bullet-head"><svg width="22" height="22" viewBox="0 0 22 22"><circle cx="11" cy="11" r="9" fill="none" stroke="#1aa0ff" stroke-width="2"/><circle cx="11" cy="11" r="4" fill="none" stroke="#1436e6" stroke-width="2"/></svg>Bullet Point 2</div>
      <ul class="sub"><li><svg width="12" height="12"><circle cx="6" cy="6" r="5" fill="none" stroke="#777"/><path d="M3.5 6l2 2 3-3.5" fill="none" stroke="#777"/></svg>Sub-bullet point</li><li><svg width="12" height="12"><circle cx="6" cy="6" r="5" fill="none" stroke="#777"/><path d="M3.5 6l2 2 3-3.5" fill="none" stroke="#777"/></svg>Sub-bullet point</li></ul>
    </div>
    <div class="bullet">
      <div class="bullet-head"><svg width="22" height="22" viewBox="0 0 22 22"><circle cx="11" cy="11" r="9" fill="none" stroke="#1aa0ff" stroke-width="2"/><circle cx="11" cy="11" r="4" fill="none" stroke="#1436e6" stroke-width="2"/></svg>Bullet Point 3</div>
      <ul class="sub"><li><svg width="12" height="12"><circle cx="6" cy="6" r="5" fill="none" stroke="#777"/><path d="M3.5 6l2 2 3-3.5" fill="none" stroke="#777"/></svg>Sub-bullet point</li><li><svg width="12" height="12"><circle cx="6" cy="6" r="5" fill="none" stroke="#777"/><path d="M3.5 6l2 2 3-3.5" fill="none" stroke="#777"/></svg>Sub-bullet point</li></ul>
    </div>
  </div>
  <div class="footer"><span class="footer-note">#Tallow Microsystems Confidential</span><span class="footer-name">Tallow</span></div>
</section>

<!-- Image left -->
<section class="slide" style="top:1754px">
  <div class="visual" style="left:0;top:57px;width:252px;height:281px;border-radius:0 40px 40px 0" role="img" aria-label="Team photograph in blue duotone"></div>
  <h2 class="title" style="left:322px;top:104px">SLIDE TITLE</h2>
  <p class="body" style="left:322px;top:150px;width:320px">Lorem ipsum dolor sit amet, consectetuer adipiscing elit, sed diam nonummy nibh euismod tincidunt ut laoreet dolore magna aliquam erat volutpat. Ut wisi enim ad minim veniam, quis nostrud exerci tation ullamcorper suscipit lobortis nisl ut aliquip ex ea</p>
  <div class="footer"><span class="footer-note">#Tallow Microsystems Confidential</span><span class="footer-name">Tallow</span></div>
</section>

<!-- Centered text -->
<section class="slide" style="top:2192px">
  <h2 class="title center" style="top:96px;text-align:center">SLIDE TITLE</h2>
  <p class="body center" style="top:144px;width:440px">Lorem ipsum dolor sit amet, consectetuer adipiscing elit, sed diam nonummy nibh euismod tincidunt ut laoreet dolore magna aliquam erat volutpat. Ut wisi enim ad minim veniam, quis nostrud exerci tation ullamcorper suscipit lobortis nisl ut aliquip ex ea</p>
  <div class="footer"><span class="footer-note">#Tallow Microsystems Confidential</span><span class="footer-name">Tallow</span></div>
</section>

<!-- Image right -->
<section class="slide" style="top:2631px">
  <h2 class="title" style="left:78px;top:106px">SLIDE TITLE</h2>
  <p class="body" style="left:78px;top:152px;width:310px">Lorem ipsum dolor sit amet, consectetuer adipiscing elit, sed diam nonummy nibh euismod tincidunt ut laoreet dolore magna aliquam erat volutpat. Ut wisi enim ad minim veniam, quis nostrud exerci tation ullamcorper suscipit lobortis nisl ut aliquip ex ea</p>
  <div class="visual" style="left:440px;top:53px;width:278px;height:286px;border-radius:40px 0 0 40px" role="img" aria-label="Team photograph in blue duotone"></div>
  <div class="footer"><span class="footer-note">#Tallow Microsystems Confidential</span><span class="footer-name">Tallow</span></div>
</section>

<!-- Charts -->
<section class="slide" style="top:3069px">
  <h2 class="title center" style="top:32px;text-align:center">SLIDE TITLE</h2>
  <p class="body center" style="top:78px;width:470px">Lorem ipsum dolor sit amet, consectetuer adipiscing elit, sed diam nonummy nibh euismod tincidunt ut laoreet dolore magna aliquam erat volutpat. Ut wisi enim ad minim veniam, quis nostrud exerci tation ullam-</p>
  <svg style="position:absolute;left:141px;top:157px" width="176" height="176" viewBox="0 0 176 176">
    <defs><linearGradient id="donutBlue" x1="0" y1="0" x2="1" y2="1"><stop offset="0" stop-color="#19b6ff"/><stop offset="1" stop-color="#1436e6"/></linearGradient></defs>
    <g transform="rotate(-90 88 88)" fill="none" stroke-width="42">
      <circle cx="88" cy="88" r="64" stroke="#1aa0ff" stroke-dasharray="18.1 384" stroke-dashoffset="0"/>
      <circle cx="88" cy="88" r="64" stroke="#1436e6" stroke-dasharray="58.3 344" stroke-dashoffset="-20.1"/>
      <circle cx="88" cy="88" r="64" stroke="#3a3a3a" stroke-dasharray="78.4 324" stroke-dashoffset="-80.4"/>
      <circle cx="88" cy="88" r="64" stroke="url(#donutBlue)" stroke-dasharray="158.8 244" stroke-dashoffset="-160.8"/>
      <circle cx="88" cy="88" r="64" stroke="#3a3a3a" stroke-dasharray="78.4 324" stroke-dashoffset="-321.6"/>
    </g>
    <g font-family="Montserrat,sans-serif" font-size="10" font-weight="700" fill="#fff">
      <text x="95" y="30">5%</text><text x="138" y="62">15%</text><text x="126" y="132">20%</text><text x="24" y="122">40%</text><text x="38" y="42">20%</text>
    </g>
  </svg>
  <svg style="position:absolute;left:370px;top:150px" width="210" height="180" viewBox="0 0 210 180">
    <g>
      <rect x="6" y="90" width="22" height="73" rx="11" fill="#3a3a3a"/>
      <rect x="50" y="26" width="22" height="137" rx="11" fill="#1436e6"/>
      <rect x="94" y="72" width="22" height="91" rx="11" fill="#3a3a3a"/>
      <rect x="138" y="54" width="22" height="109" rx="11" fill="#1aa0ff"/>
      <rect x="182" y="123" width="22" height="40" rx="11" fill="#3a3a3a"/>
    </g>
    <g font-family="Montserrat,sans-serif" font-size="9" font-weight="700" fill="#fff">
      <text transform="translate(21 140) rotate(-90)">40%</text>
      <text transform="translate(65 140) rotate(-90)">75%</text>
      <text transform="translate(109 140) rotate(-90)">50%</text>
      <text transform="translate(153 140) rotate(-90)">60%</text>
      <text transform="translate(197 154) rotate(-90)">22%</text>
    </g>
    <g font-family="Montserrat,sans-serif" font-size="7" font-weight="600" fill="#555" text-anchor="middle">
      <text x="17" y="175">2018</text><text x="61" y="175">2019</text><text x="105" y="175">2020</text><text x="149" y="175">2021</text><text x="193" y="175">2022</text>
    </g>
  </svg>
  <div class="footer"><span class="footer-note">#Tallow Microsystems Confidential</span><span class="footer-name">Tallow</span></div>
</section>

<!-- Break -->
<section class="slide" style="top:3508px">
  <div class="break-pill">Break</div>
  <div class="break-mug" role="img" aria-label="Photograph of a coffee mug"></div>
  <div class="footer"><span class="footer-note">#Tallow Microsystems Confidential</span><span class="footer-name">Tallow</span></div>
</section>

<!-- Title only -->
<section class="slide" style="top:3947px">
  <h2 class="title center" style="top:144px;text-align:center">SLIDE TITLE</h2>
  <div class="footer"><span class="footer-note">#Tallow Microsystems Confidential</span><span class="footer-name">Tallow</span></div>
</section>

<!-- Closing -->
<section class="slide" style="top:4386px">
  <div class="closing">Tallow Microsystems</div>
  <div class="footer"><span class="footer-note">#Tallow Microsystems Confidential</span><span class="footer-name">Tallow</span></div>
</section>

</body>
</html>
```